Counseling Practice Business Card

I need a professional looking business card incorporating my new logo that was just completed. Card needs to incorporate my name and title, description of my specialty, my address, my phone number, my fax number, my email and my website URL. I need to be able to choose design on/with different paper colors and textures.
I do not have a lot of business card ideas so I am open to anything but I want bold,sharp, clear card without additional designs other than my logo (see attached file info). I am open to different color backgrounds or paper colors including black. I do not like traditional brackets around area codes in phone number or dashes between numbers in phone number. Am open to other ways of presenting including periods between numbers as appropriate. I do not know enough to know what I like yet but I want card to coordinate and work together with my logo. My practice emphasizes natural mental health interventions so any use of color (with background paper color or the blue and green in my logo) that elicits nature is nice. In addition to black, any natural brown or wood looking background might be desirable also. Most of the offerings so far look very similar and boring.

Target Market(s)

Potential therapy clients and other professionals

Contact Information for Business Card

Card information:
Marcus T. Whitfield, Ph.D.
Licensed Clinical Psychologist
Integrative Health Coach
4812 Ferndale Pkwy NW
Suite 730
Duluth, GA 30096
(770) 555-0142 phone
(770) 555-0186 fax
drmarcuswhitfield@kelvora.com
pathbloomcounseling.com

Font styles to use
Serif
Sans Serif
Other font styles liked:
• anything that you think looks crisp, clear and easily readable

Requirements
Must have
• Any color used should coordinate with my logo design (see attached files).
• Card should be printed horizontally so top and bottom are longest sides of rectangle.
• Background color or paper color should complement and highlight logo. Do not like a white background. black, grey, brown or any color my logo would blend well with.
Nice to have
• I would like designer to utilize color to highlight letters/name or phone-fax-web symbols.
• Bottom edge of card could be highlighted if appropriate to an idea.
Should not have
• I would NOT want the card to have a pure white background at all.
• No clear cards.
• Cards should be oriented with long sides on bottom and top, NOT sides. DO NOT LIKE THIS THIN TALL ORIENTATION.

```html
<!DOCTYPE html>
<html lang="en">
<head>
<meta charset="utf-8">
<title>Pathbloom Counseling – Business Card</title>
<link rel="stylesheet" href="https://fonts.googleapis.com/css2?family=Montserrat:wght@500;600;700&family=Open+Sans:wght@400;700&display=swap">
<style>
  :root {
    --backdrop: #3b3d40;
    --paper: #edbf91;
    --brand-blue: #1b76be;
    --brand-green: #1e7a34;
    --ink: #3a332c;
    --white: #ffffff;
  }
  * { box-sizing: border-box; margin: 0; padding: 0; }
  html, body { width: 1200px; height: 928px; overflow: hidden; }
  body {
    background: var(--backdrop);
    font-family: "Open Sans", Arial, sans-serif;
    position: relative;
  }
  .card {
    position: absolute;
    left: 240px;
    width: 720px;
    height: 411px;
    background: var(--paper);
    box-shadow: 0 10px 30px rgba(0,0,0,.35);
    overflow: hidden;
  }
  .card--front { top: 36px; }
  .card--details { top: 481px; }

  .brand {
    display: flex;
    align-items: center;
    gap: 12px;
    font-family: "Montserrat", Arial, sans-serif;
    font-weight: 600;
    color: var(--brand-blue);
    white-space: nowrap;
  }
  .brand__dot {
    border-radius: 50%;
    background: var(--brand-blue);
  }

  /* Front */
  .card--front .brand {
    position: absolute;
    top: 140px; left: 0; right: 0;
    justify-content: center;
    font-size: 46px;
  }
  .card--front .brand__dot { width: 26px; height: 26px; }
  .front__url {
    position: absolute;
    bottom: 70px; left: 0; right: 0;
    text-align: center;
    font-size: 17px;
    color: var(--brand-blue);
    letter-spacing: .3px;
  }

  /* Details */
  .card--details .brand {
    position: absolute;
    top: 50px; left: 190px;
    font-size: 36px;
  }
  .card--details .brand__dot { width: 20px; height: 20px; }
  .specialty {
    position: absolute;
    top: 150px; left: 118px;
    font-family: "Montserrat", Arial, sans-serif;
    font-weight: 700;
    font-size: 22px;
    color: var(--ink);
    letter-spacing: -.2px;
  }
  .person {
    position: absolute;
    top: 222px; left: 40px;
    width: 322px;
    text-align: right;
  }
  .person__name {
    font-family: "Montserrat", Arial, sans-serif;
    font-weight: 700;
    font-size: 21px;
    color: var(--brand-green);
    white-space: nowrap;
  }
  .person__title {
    margin-top: 4px;
    font-family: "Montserrat", Arial, sans-serif;
    font-weight: 500;
    font-size: 15px;
    color: var(--ink);
  }
  .divider {
    position: absolute;
    left: 378px; top: 205px;
    width: 1.5px; height: 120px;
    background: var(--brand-green);
  }
  .contacts {
    position: absolute;
    left: 396px; top: 206px;
    list-style: none;
  }
  .contacts li {
    display: flex;
    align-items: center;
    gap: 10px;
    height: 29px;
    font-size: 14.5px;
    color: var(--ink);
  }
  .contacts svg { width: 14px; height: 14px; fill: var(--brand-green); flex: none; }
  .address-band {
    position: absolute;
    left: 0; right: 0; bottom: 0;
    height: 62px;
    background: var(--brand-blue);
    display: flex;
    align-items: center;
    justify-content: center;
    gap: 10px;
    color: var(--white);
    font-weight: 700;
    font-size: 18px;
    letter-spacing: .4px;
  }
  .address-band svg { width: 14px; height: 18px; fill: var(--white); }
</style>
</head>
<body>

<section class="card card--front">
  <div class="brand"><span class="brand__dot"></span>Pathbloom Counseling</div>
  <p class="front__url">www.pathbloomcounseling.com</p>
</section>

<section class="card card--details">
  <div class="brand"><span class="brand__dot"></span>Pathbloom Counseling</div>
  <p class="specialty">INTEGRATIVE HEALTH COACH</p>

  <div class="person">
    <p class="person__name">Marcus T. Whitfield, Ph.D.</p>
    <p class="person__title">Licensed Clinical Psychologist</p>
  </div>

  <span class="divider"></span>

  <ul class="contacts">
    <li>
      <svg viewBox="0 0 16 16" aria-hidden="true"><path d="M3.5 1h3l1 4-2 1.2a9 9 0 0 0 4.3 4.3L11 8.5l4 1v3c0 1-1 2-2 2A12 12 0 0 1 1.5 3c0-1 1-2 2-2z"/></svg>
      (770) 555-0142
    </li>
    <li>
      <svg viewBox="0 0 16 16" aria-hidden="true"><path d="M4 1h6l2 2v3H4zM2 7h12v7H2zm3 2v1h2V9zm4 0v1h2V9zm-4 2v1h2v-1zm4 0v1h2v-1z"/></svg>
      (770) 555-0186
    </li>
    <li>
      <svg viewBox="0 0 16 16" aria-hidden="true"><path d="M1 3h14v10H1zm1.5 1.2v.4L8 8.5l5.5-3.9v-.4z"/></svg>
      drmarcuswhitfield@kelvora.com
    </li>
    <li>
      <svg viewBox="0 0 16 16" aria-hidden="true"><path d="M8 1a7 7 0 1 0 0 14A7 7 0 0 0 8 1zm0 1.5c.8 0 1.7 1.5 2 4H6c.3-2.5 1.2-4 2-4zM6 8h4c-.1 3-1.1 5.5-2 5.5S6.1 11 6 8z"/></svg>
      pathbloomcounseling.com
    </li>
  </ul>

  <div class="address-band">
    <svg viewBox="0 0 14 18" aria-hidden="true"><path d="M7 0a7 7 0 0 0-7 7c0 5 7 11 7 11s7-6 7-11a7 7 0 0 0-7-7zm0 4.5a2.5 2.5 0 1 1 0 5 2.5 2.5 0 0 1 0-5z"/></svg>
    4812 Ferndale Pkwy NW Suite 730 Duluth, GA 30096
  </div>
</section>

</body>
</html>
```